Flyer Design Project

We are a coaching organisation that is about to launch classes catering to local and international university students in Australia. We would like a flyer that is fresh, captivating and ultimately pushes people to our website.
To understand the artistic approach to our business, visit our website: www.brightlanetutors.com.au
Updates
Hi designers, we have changed the criteria slightly to give you more creative license... Feel free to ask any questions, all the best.
Target Market(s)
International University Students aged between 18-25
Industry/Entity Type
University
Requirements
Must have
- Size: 1 sided A5 flyer
Must have logo on page
Introductory offer of 20% off all courses
Bright Lane Tutors exists to help university students with real life skill development such as public speaking. We aim to equip students with skills that are not taught in the university environment to enable them to maximise their results.
To find out more visit: www.brightlanetutors.com.au
CONTACT DETAILS: Leave space for 10 digit phone number
Nice to have
- Bold, eye catching design
Fresh, fun and professional look
Good use of typography
Should not have
- Do not use colours outside or that do not compliment our colour palette. You can view our three main colours (blue, pink, yellow) on our website.
www.brightlanetutors.com.au/courses/publicspeaking

```html
<!DOCTYPE html>
<html lang="en">
<head>
<meta charset="utf-8">
<title>Bright Lane Tutors – Introductory Offer Flyer</title>
<link href="https://fonts.googleapis.com/css2?family=Cabin:wght@700&family=Arimo:wght@400;700&display=swap" rel="stylesheet">
<style>
  :root {
    --canvas-grey: #cccccc;
    --sky-blue: #4fb4fd;
    --sunny-yellow: #ffe74f;
    --text-yellow: #f4f03c;
    --coral-pink: #f74f7a;
    --navy: #2f3a86;
    --white: #ffffff;
  }
  * { margin: 0; padding: 0; box-sizing: border-box; }
  html, body { width: 1200px; height: 1000px; overflow: hidden; }
  body { background: var(--canvas-grey); position: relative; font-family: "Arimo", Arial, sans-serif; }

  .flyer { position: absolute; left: 295px; top: 45px; width: 636px; height: 902px; }
  .block { position: absolute; }
  .block--white  { left: 0; top: 0; width: 218px; height: 482px; background: var(--white); }
  .block--yellow { left: 0; top: 482px; width: 218px; height: 268px; background: var(--sunny-yellow); }
  .block--blue   { left: 218px; top: 0; width: 418px; height: 750px; background: var(--sky-blue); }
  .block--pink   { left: 0; top: 750px; width: 636px; height: 152px; background: var(--coral-pink); }

  .brand { position: absolute; left: 16px; top: 244px; display: flex; align-items: center; gap: 8px; }
  .brand__dot { width: 34px; height: 34px; border-radius: 50%; background: var(--navy); flex: none; }
  .brand__name { font-family: "Arimo", Arial, sans-serif; font-weight: 400; font-size: 25px; line-height: 28px; color: var(--navy); }

  .t { position: absolute; white-space: nowrap; line-height: 1; }
  .center { transform: translateX(-50%); }
  .headline { font-family: "Cabin", "Trebuchet MS", sans-serif; font-weight: 700; }
  .hl-yellow { color: var(--text-yellow); font-size: 33px; }
  .offer-figure { color: var(--white); font-size: 64px; }
  .brand-title { color: var(--white); font-size: 35px; }
  .body-copy { color: var(--text-yellow); font-size: 19px; }
  .shout { color: var(--white); font-size: 32px; font-family: "Arimo", Arial, sans-serif; }

  .footer-line { font-family: "Cabin", "Trebuchet MS", sans-serif; font-weight: 700; font-size: 19px; color: var(--white); }

  .divider { position: absolute; left: 250px; top: 255px; }
</style>
</head>
<body>
  <main class="flyer">
    <div class="block block--white"></div>
    <div class="block block--yellow"></div>
    <div class="block block--blue"></div>
    <div class="block block--pink"></div>

    <div class="brand">
      <span class="brand__dot"></span>
      <span class="brand__name">Bright Lane<br>Tutors</span>
    </div>

    <p class="t center headline hl-yellow" style="left:432px; top:62px;">Introductory offer of</p>
    <p class="t center headline offer-figure" style="left:432px; top:118px;">20%</p>
    <p class="t center headline hl-yellow" style="left:432px; top:194px;">off all courses</p>

    <svg class="divider" width="350" height="36" viewBox="0 0 350 36" aria-hidden="true">
      <line x1="5" y1="18" x2="148" y2="18" stroke="var(--coral-pink)" stroke-width="4"/>
      <line x1="205" y1="18" x2="348" y2="18" stroke="var(--coral-pink)" stroke-width="4"/>
      <circle cx="177" cy="18" r="14" fill="none" stroke="var(--coral-pink)" stroke-width="2"/>
      <circle cx="177" cy="18" r="10" fill="none" stroke="var(--coral-pink)" stroke-width="2"/>
      <circle cx="177" cy="18" r="6" fill="var(--coral-pink)"/>
    </svg>

    <h1 class="t center headline brand-title" style="left:423px; top:330px;">Bright Lane Tutors</h1>

    <p class="t center body-copy" style="left:418px; top:379px;">exists tp help university students</p>
    <p class="t center body-copy" style="left:418px; top:406px;">with real life skill development</p>
    <p class="t body-copy" style="left:283px; top:463px;">such as</p>
    <p class="t shout" style="left:378px; top:440px;">PUBLIC</p>
    <p class="t shout" style="left:377px; top:484px;">SPEAKING.</p>
    <p class="t center body-copy" style="left:432px; top:527px;">We aim to equip students with skills</p>
    <p class="t center body-copy" style="left:411px; top:553px;">that are not taught in</p>
    <p class="t center body-copy" style="left:419px; top:579px;">the university environment to</p>
    <p class="t body-copy" style="left:254px; top:620px;">enable them to</p>
    <p class="t shout" style="left:415px; top:609px;">maximise</p>
    <p class="t body-copy" style="left:475px; top:646px;">their results.</p>

    <p class="t footer-line" style="left:54px; top:788px;">To find out more visit: www.brightlanetutors.com.au</p>
    <p class="t footer-line" style="left:54px; top:840px;">CONTACT DETAILS:</p>
  </main>
</body>
</html>
```